Infographics for Vextora reports

Vextora report is a summary of software developer skills.

Main purpose of our reports is to provide quick and easy insight into skill set of tested individual.
Our mission is to help talents to stand out.

Our target market is a male between 25-40, bit of a nerd, who likes technology and computer games.
The report should communicate quality and trust.

Report should fit on one A4 page and contain the following
1. Company logo - provided with the brief

2. Information about tested developer:
- Photo of developer
- Full name
- Location
- Email

3. How he or she compares against the average Software Developer:
- Collaboration ranking (0-100)
- Skills ranking by languages (up to 10 languages)

4. Total ranking - Number 1-100% which should stand out as a quick reference

We would like to included some sort of stamp of approval on the report.
The stamp would contain the overall score of a developer (The Total ranking from point 4.) .

As an option we were considering to use some sort of categorisation for the total ranking.
Here are examples of Vextora categories:
Wizard of Vextora for ranking between 90% – 100%
Scholar of Vextora for ranking between 80% - 89%
Knight of Vextora for ranking between 70% - 79%
Warrior of Vextora for ranking between 60% - 69%
Rebel of Vextora unknown or under 60%

Developer would belong to one of the categories depending on their Total ranking.

We are not very fixed on category names. We would be happy to consider any other option.

Here are some example data for the report:

The average Software Developer ranking is 50%.

Tested Developer:
Photo
Full name: Marek Tollan
Location: Sydney, Australia
Email: marek.tollan@postbox-mail.net

Collaboration ranking: 95%

Skills:
Language: C++
Number of Open Source Projects: 5
Ranking: 91%

Language: Javascript
Number of Open Source Projects: 3
Ranking: 81%

Language: Python
Number of Open Source Projects: 1
Ranking: 31%

Language: Ruby
Number of Open Source Projects: 2
Ranking: 25%

Language: C#
Ranking: 85%

Language: Java
Ranking: 75%

Total Ranking: 75% - Knight of Vextora

Thank you!

```html
<!DOCTYPE html>
<html lang="en">
<head>
<meta charset="utf-8">
<title>Vextora Report – Marek Tollan</title>
<link href="https://fonts.googleapis.com/css2?family=Montserrat:wght@400;700;800;900&family=Open+Sans:wght@300;400&family=Black+Ops+One&display=swap" rel="stylesheet">
<style>
  :root {
    --purple: #8f2a79;
    --purple-dark: #6f1d5d;
    --black: #0b0b0b;
    --grey-band: #d2d3d5;
    --grey-label: #c9cacc;
    --grey-hatch: #b9babc;
    --grey-faint: #f1f1f2;
    --white: #ffffff;
    --text: #111111;
  }
  html, body { margin: 0; padding: 0; overflow: hidden; background: var(--white); }
  .report {
    position: relative; width: 848px; height: 1200px; overflow: hidden;
    background: var(--white); font-family: "Montserrat", Arial, sans-serif; color: var(--text);
  }
  .abs { position: absolute; }

  /* Top bar */
  .top-bar { left: 0; top: 0; width: 848px; height: 85px; background: var(--black); }
  .report-title { left: 34px; top: 22px; margin: 0; color: var(--white); font-weight: 900; font-size: 20px; letter-spacing: 0.5px; text-transform: uppercase; line-height: 1; }
  .report-note { left: 34px; top: 46px; margin: 0; color: var(--white); font-family: "Open Sans", Arial, sans-serif; font-size: 10.5px; line-height: 1; }
  .brand { right: 36px; top: 20px; display: flex; align-items: center; gap: 10px; }
  .brand-mark { width: 38px; height: 38px; background: var(--purple); }
  .brand-name { color: var(--white); font-weight: 800; font-size: 32px; line-height: 1; }

  /* Profile header */
  .profile-band { left: 0; top: 85px; width: 848px; height: 240px; background: var(--grey-band); }
  .photo-frame {
    left: 29px; top: 109px; width: 178px; height: 174px; box-sizing: border-box;
    border: 7px solid var(--black); border-radius: 26px; background: var(--white); padding: 8px;
  }
  .photo-frame .photo { width: 100%; height: 100%; border-radius: 14px; background: linear-gradient(180deg, #ffffff 0%, #e7d3e2 60%, var(--purple) 100%); }
  .frame-pointer { left: 100px; top: 306px; }
  .tested-label { left: 249px; top: 126px; margin: 0; font-size: 15px; font-weight: 400; }
  .developer-name { left: 247px; top: 140px; margin: 0; font-size: 50px; font-weight: 800; line-height: 1.1; letter-spacing: -0.5px; }
  .contact { top: 210px; display: flex; align-items: center; gap: 9px; font-family: "Open Sans", Arial, sans-serif; font-size: 16px; }
  .contact-location { left: 247px; }
  .contact-email { left: 455px; }
  .collaboration { left: 254px; top: 247px; margin: 0; font-size: 19px; font-weight: 400; }

  /* Skills heading */
  .skills-band { left: 0; top: 324px; width: 848px; height: 63px; background: var(--purple); }
  .skills-title { left: 0; top: 324px; width: 848px; margin: 0; line-height: 63px; text-align: center; color: var(--white); font-size: 37px; font-weight: 800; letter-spacing: 0.5px; }

  /* Background shapes */
  .backdrop { left: 0; top: 387px; }

  /* Skill rows */
  .axis { left: 289px; top: 444px; width: 11px; height: 540px; background: var(--black); }
  .skill { left: 0; width: 848px; height: 64px; }
  .skill-name { position: absolute; right: 572px; top: 10px; margin: 0; font-size: 35px; font-weight: 800; line-height: 44px; text-align: right; white-space: nowrap; }
  .metric-label {
    position: absolute; left: 313px; height: 27px; line-height: 27px; padding-left: 9px; box-sizing: border-box;
    font-family: "Open Sans", Arial, sans-serif; font-size: 17px; font-weight: 300; color: var(--text);
  }
  .projects-label { top: 0; width: 202px; background: var(--grey-label); }
  .project-count { position: absolute; left: 523px; top: 0; height: 27px; display: flex; align-items: center; gap: 5px; font-family: "Open Sans", Arial, sans-serif; font-size: 16px; }
  .project-dot { width: 23px; height: 23px; border-radius: 50%; background: var(--purple); }
  .ranking-track {
    position: absolute; left: 313px; top: 36px; width: 334px; height: 27px;
    background: repeating-linear-gradient(135deg, var(--grey-hatch) 0 3px, var(--white) 3px 6px);
  }
  .ranking-fill { height: 100%; background: var(--purple); }
  .ranking-track .metric-label { left: 0; top: 0; color: var(--white); }
  .ranking-value { position: absolute; left: 651px; top: 36px; line-height: 27px; font-family: "Open Sans", Arial, sans-serif; font-size: 17px; }

  /* Footer */
  .footer-band { left: 0; top: 1120px; width: 848px; height: 60px; background: var(--grey-faint); }
  .footer-bar { left: 0; top: 1180px; width: 848px; height: 20px; background: var(--black); }
  .footer-pointer { left: 105px; top: 1164px; }

  /* Total */
  .summary { position: relative; z-index: 2; }
  .total { left: 193px; top: 1015px; display: flex; align-items: center; gap: 8px; font-size: 17px; font-weight: 700; }
  .category { color: var(--purple); font-weight: 800; }
  .category-badge { width: 22px; height: 26px; }

  /* Stamp */
  .score-seal { left: 643px; top: 988px; width: 106px; height: 106px; }
  .approved-stamp {
    left: 612px; top: 1062px; transform: rotate(-13deg); transform-origin: center;
    border: 5px solid var(--purple); border-radius: 8px; padding: 2px 12px;
    font-family: "Black Ops One", Impact, sans-serif; font-size: 34px; color: var(--purple); letter-spacing: 1px; line-height: 1.1;
    white-space: nowrap; opacity: 0.92;
  }
</style>
</head>
<body>
<main class="report">
  <header>
    <div class="abs top-bar"></div>
    <h1 class="abs report-title">Vextora Report</h1>
    <p class="abs report-note">* The average Software Developer ranking is 50%.</p>
    <div class="abs brand"><span class="brand-mark"></span><span class="brand-name">Vextora</span></div>
  </header>

  <section class="profile">
    <div class="abs profile-band"></div>
    <div class="abs photo-frame"><div class="photo" role="img" aria-label="Photo of the tested developer"></div></div>
    <p class="abs tested-label">Tested Developer:</p>
    <h2 class="abs developer-name">Marek Tollan</h2>
    <div class="abs contact contact-location">
      <svg width="15" height="21" viewBox="0 0 15 21" aria-hidden="true"><path d="M7.5 0C3.4 0 0 3.3 0 7.4 0 12.9 7.5 21 7.5 21S15 12.9 15 7.4C15 3.3 11.6 0 7.5 0Zm0 10.4a3 3 0 1 1 0-6 3 3 0 0 1 0 6Z" fill="#111"/></svg>
      <span>Sydney, Australia</span>
    </div>
    <div class="abs contact contact-email">
      <svg width="24" height="17" viewBox="0 0 24 17" aria-hidden="true"><rect width="24" height="17" fill="#111"/><path d="M1 1l11 9 11-9" fill="none" stroke="#d2d3d5" stroke-width="1.6"/></svg>
      <span>marek.tollan@postbox-mail.net</span>
    </div>
    <p class="abs collaboration">Collaboration Ranking: 95%</p>
  </section>

  <svg class="abs backdrop" width="848" height="730" aria-hidden="true">
    <polygon points="400,0 848,0 848,120 560,230" fill="#f5f5f6"/>
    <polygon points="120,20 300,120 160,300 0,200 0,60" fill="#f7f7f8"/>
    <polygon points="560,380 848,250 848,560" fill="#f6f6f7"/>
    <polygon points="0,520 220,460 300,640 0,700" fill="#f7f7f8"/>
  </svg>

  <section class="skills">
    <div class="abs skills-band"></div>
    <h2 class="abs skills-title">SKILLS</h2>
    <svg class="abs frame-pointer" width="36" height="19" aria-hidden="true"><polygon points="18,0 36,19 0,19" fill="#8f2a79"/></svg>

    <div class="abs axis"></div>

    <div class="abs skill" style="top:457px">
      <h3 class="skill-name">C++</h3>
      <div class="metric-label projects-label">Open Source Projects</div>
      <div class="project-count"><span class="project-dot"></span><span class="project-dot"></span><span class="project-dot"></span><span class="project-dot"></span><span class="project-dot"></span><span>(5)</span></div>
      <div class="ranking-track"><div class="ranking-fill" style="width:91%"></div><div class="metric-label">Ranking</div></div>
      <span class="ranking-value">91%</span>
    </div>

    <div class="abs skill" style="top:548px">
      <h3 class="skill-name">Javascript</h3>
      <div class="metric-label projects-label">Open Source Projects</div>
      <div class="project-count"><span class="project-dot"></span><span class="project-dot"></span><span class="project-dot"></span><span>(3)</span></div>
      <div class="ranking-track"><div class="ranking-fill" style="width:81%"></div><div class="metric-label">Ranking</div></div>
      <span class="ranking-value">81%</span>
    </div>

    <div class="abs skill" style="top:639px">
      <h3 class="skill-name">Python</h3>
      <div class="metric-label projects-label">Open Source Projects</div>
      <div class="project-count"><span class="project-dot"></span><span>(1)</span></div>
      <div class="ranking-track"><div class="ranking-fill" style="width:31%"></div><div class="metric-label">Ranking</div></div>
      <span class="ranking-value">31%</span>
    </div>

    <div class="abs skill" style="top:729px">
      <h3 class="skill-name">Ruby</h3>
      <div class="metric-label projects-label">Open Source Projects</div>
      <div class="project-count"><span class="project-dot"></span><span class="project-dot"></span><span>(2)</span></div>
      <div class="ranking-track"><div class="ranking-fill" style="width:25%"></div><div class="metric-label">Ranking</div></div>
      <span class="ranking-value">25%</span>
    </div>

    <div class="abs skill" style="top:820px">
      <h3 class="skill-name">C#</h3>
      <div class="metric-label projects-label">Open Source Projects</div>
      <div class="project-count"><span class="project-dot"></span><span class="project-dot"></span><span class="project-dot"></span><span>(3)</span></div>
      <div class="ranking-track"><div class="ranking-fill" style="width:85%"></div><div class="metric-label">Ranking</div></div>
      <span class="ranking-value">85%</span>
    </div>

    <div class="abs skill" style="top:911px">
      <h3 class="skill-name">Java</h3>
      <div class="metric-label projects-label">Open Source Projects</div>
      <div class="project-count"><span class="project-dot"></span><span class="project-dot"></span><span class="project-dot"></span><span class="project-dot"></span><span class="project-dot"></span><span>(5)</span></div>
      <div class="ranking-track"><div class="ranking-fill" style="width:75%"></div><div class="metric-label">Ranking</div></div>
      <span class="ranking-value">75%</span>
    </div>
  </section>

  <footer>
    <div class="abs footer-band"></div>
    <svg class="abs footer-pointer" width="30" height="17" aria-hidden="true"><polygon points="15,0 30,17 0,17" fill="#0b0b0b"/></svg>
    <div class="abs footer-bar"></div>
  </footer>

  <section class="summary">
    <div class="abs total">
      <span>Total Ranking: 75% |</span>
      <svg class="category-badge" viewBox="0 0 22 26" aria-hidden="true"><path d="M11 0 22 4v9c0 7-5 11-11 13C5 24 0 20 0 13V4Z" fill="#8f2a79"/></svg>
      <span class="category">Knight of Vextora</span>
    </div>

    <svg class="abs score-seal" viewBox="0 0 96 96" aria-label="Total score 75">
      <circle cx="48" cy="48" r="46" fill="#0b0b0b"/>
      <circle cx="48" cy="48" r="38" fill="#ffffff"/>
      <circle cx="48" cy="48" r="34" fill="none" stroke="#0b0b0b" stroke-width="1.5"/>
      <g fill="#ffffff">
        <circle cx="48" cy="6" r="2"/><circle cx="27" cy="12" r="2"/><circle cx="69" cy="12" r="2"/>
        <circle cx="12" cy="27" r="2"/><circle cx="84" cy="27" r="2"/><circle cx="7" cy="48" r="2"/><circle cx="89" cy="48" r="2"/>
      </g>
      <text x="48" y="60" text-anchor="middle" font-family="Montserrat, Arial, sans-serif" font-weight="900" font-size="34" fill="#0b0b0b">75</text>
    </svg>
    <div class="abs approved-stamp">APPROVED</div>
  </section>
</main>
</body>
</html>
```